IT consultancy business needs logo and business card designed

I need designed business card. it needs to have some wow effect, but simple, corporate and business focused. We provide corporate grade IT services to medium size businesses. These services are IT support over phone, email, in person, VOIP services, IT security , networking - everything that helps business be productivy.

Out tag line will be something along these lines" promoting business growth through use of technology:.

I need a logo designed as well. I am happy to use any colors/theme, perhaps neutral colours, earthy?

Priority: NICE looking, wow design, nice fonts, colors etc... nice logo, business focused but HAS to be modern, wow effect. I will accept anything that looks really cool.

Target Market(s)

Target market are businesses with 20-100 employees. Audience are business decision makers, like general managers, CEO, directors, those are the one seeing this business card;

Industry/Entity Type

Business

Contact Information for Business Card

I am totally flexible, suprise me me something creative:

Miroslav Penkov logo on this side(you will design)
managing director ------------------------------- this is line
slogan: technology.delivered.simple

Level 5, 42 Whitmore Lane, Sydney, NSW 2000
miroslav@vontiq.com.au
www.vontiq.com.au

back page: logo and slogan: promoting business growth through use of technolog

Requirements
Must have
• Must look modern, cool., wow effect, yet simple and professional.

```html
<!DOCTYPE html>
<html lang="en">
<head>
<meta charset="utf-8">
<title>Vontiq Business Card</title>
<link href="https://fonts.googleapis.com/css2?family=Michroma&family=Exo+2:wght@400&display=swap" rel="stylesheet">
<style>
  :root {
    --page: #e9eaec;
    --card: #ffffff;
    --blue-light: #4f80bd;
    --blue-dark: #1f4678;
    --stripe: #3a3c40;
    --brand: #2a5f9e;
    --tag: #3b3d42;
    --ink-light: #ffffff;
  }
  * { margin: 0; padding: 0; box-sizing: border-box; }
  html, body {
    width: 1200px; height: 901px; overflow: hidden;
    background: var(--page);
  }
  .sheet {
    position: relative; width: 1200px; height: 901px;
    display: flex; align-items: center; justify-content: center; gap: 50px;
  }
  .card {
    position: relative; width: 525px; height: 300px;
    background: var(--card); border-radius: 26px; overflow: hidden;
    box-shadow: 0 10px 30px rgba(0,0,0,0.15);
  }
  .card-wave { position: absolute; inset: 0; }
  .brand {
    position: absolute; left: 150px; top: 56px;
    display: flex; align-items: center; gap: 14px;
  }
  .brand-mark {
    width: 22px; height: 22px; border-radius: 50%;
    background: var(--brand);
  }
  .brand-name {
    font-family: "Michroma", sans-serif; font-size: 38px; letter-spacing: 3px;
    color: var(--brand); line-height: 1;
  }
  .brand-tag {
    position: absolute; left: 186px; top: 108px;
    font-family: "Exo 2", sans-serif; font-size: 17px;
    color: var(--tag); letter-spacing: 1px;
  }
  .contact {
    position: absolute; font-family: "Michroma", sans-serif;
    color: var(--ink-light); font-size: 8.5px; letter-spacing: 1.2px; line-height: 1.75;
  }
  .contact-person { left: 34px; top: 200px; width: 230px; }
  .person-name { font-size: 11px; letter-spacing: 2px; }
  .person-title { margin-bottom: 8px; }
  .contact-lines { left: 280px; top: 200px; list-style: none; }
  .contact-lines li { display: flex; align-items: center; gap: 7px; }
  .contact-lines svg { width: 11px; height: 11px; flex: none; }
  .card-back .brand-back {
    position: absolute; inset: 0;
    display: flex; align-items: center; justify-content: center; gap: 16px;
  }
  .card-back .brand-mark { width: 26px; height: 26px; }
</style>
</head>
<body>
<main class="sheet">
  <section class="card card-front" aria-label="Business card front">
    <svg class="card-wave" viewBox="0 0 525 300" preserveAspectRatio="none" aria-hidden="true">
      <defs>
        <linearGradient id="bandBlue" x1="0" y1="0" x2="0.3" y2="1">
          <stop offset="0" stop-color="var(--blue-light)"/>
          <stop offset="1" stop-color="var(--blue-dark)"/>
        </linearGradient>
      </defs>
      <path d="M0 150 C120 128 230 150 320 172 C410 194 470 196 525 184 L525 300 L0 300 Z" fill="var(--stripe)"/>
      <path d="M0 158 C120 138 230 160 320 182 C410 204 470 206 525 196 L525 300 L0 300 Z" fill="url(#bandBlue)"/>
    </svg>
    <div class="brand">
      <span class="brand-mark" aria-hidden="true"></span>
      <span class="brand-name">VONTIQ</span>
    </div>
    <p class="brand-tag">technology.delivered.simple</p>
    <div class="contact contact-person">
      <p class="person-name">MIROSLAV PENKOV</p>
      <p class="person-title">Managing Director</p>
      <p>Level 5, 42 Whitmore Lane,</p>
      <p>Sydney, NSW 2000</p>
    </div>
    <ul class="contact contact-lines">
      <li><svg viewBox="0 0 12 12" aria-hidden="true"><circle cx="6" cy="6" r="6" fill="#fff"/><path d="M4 3.2l1 1.3-.6.8c.4.8 1 1.4 1.8 1.8l.8-.6 1.3 1-.6 1c-2.4-.2-4.3-2.1-4.5-4.5z" fill="var(--blue-dark)"/></svg>02 9555 0142</li>
      <li><svg viewBox="0 0 12 12" aria-hidden="true"><circle cx="6" cy="6" r="6" fill="#fff"/><rect x="4.2" y="2.6" width="3.6" height="6.8" rx="0.6" fill="var(--blue-dark)"/></svg>0412 555 318</li>
      <li><svg viewBox="0 0 12 12" aria-hidden="true"><circle cx="6" cy="6" r="6" fill="#fff"/><rect x="3" y="4" width="6" height="4.2" fill="none" stroke="var(--blue-dark)" stroke-width="0.9"/><path d="M3 4l3 2.3L9 4" fill="none" stroke="var(--blue-dark)" stroke-width="0.9"/></svg>miroslav@vontiq.com.au</li>
      <li><svg viewBox="0 0 12 12" aria-hidden="true"><circle cx="6" cy="6" r="6" fill="#fff"/><circle cx="6" cy="6" r="3.2" fill="none" stroke="var(--blue-dark)" stroke-width="0.8"/><path d="M2.8 6h6.4M6 2.8c-1.4 1.8-1.4 4.6 0 6.4M6 2.8c1.4 1.8 1.4 4.6 0 6.4" fill="none" stroke="var(--blue-dark)" stroke-width="0.7"/></svg>www.vontiq.com.au</li>
    </ul>
  </section>

  <section class="card card-back" aria-label="Business card back">
    <div class="brand-back">
      <span class="brand-mark" aria-hidden="true"></span>
      <span class="brand-name">VONTIQ</span>
    </div>
  </section>
</main>
</body>
</html>
```